Business card to be used as a flyer

This business card should do the trick of a full scale flyer , so basicaly from the business card itself we only keep the size and remove the clasical name , position , company name (etc).
This business cards should be , like said above, used as promo tool, being gived to different girls . So base one : the design is girls oriented.
Colors : black background . We will use gold (color) folio for the text.
Attached you have our logo, but this should not be a proiminent part of the design . You can use only the cat head instead.
Target Market(s)
Girls / Women
Contact Information for Business Card
> black background , gold / folio text and elements
> cat head from the logo in a creative way do be displayed
> proieminent text "your path to success starts here"
> contact details phone and website .
www.velvadrome.ro (website) and 0741263519 (phone)
Font styles to use
Colors
Designer to choose only greyscale colors for use in the design.
Look and feel

```html
<!DOCTYPE html>
<html lang="en">
<head>
<meta charset="utf-8">
<title>Velvadrome Studio — Business Card</title>
<link rel="stylesheet" href="https://fonts.googleapis.com/css2?family=Arimo:wght@400;700&display=swap">
<style>
  :root {
    --backdrop: #e6e6e4;
    --card-black: #1c1c1c;
    --card-black-deep: #121212;
    --gold: #c9a14a;
    --gold-light: #e8d392;
    --gold-dark: #9c7424;
    --band-text: #2a2112;
  }
  * { margin: 0; padding: 0; box-sizing: border-box; }
  html, body { width: 1200px; height: 801px; overflow: hidden; }
  body {
    background: var(--backdrop);
    font-family: "Arimo", Arial, sans-serif;
    position: relative;
  }
  .card {
    position: absolute;
    width: 540px;
    height: 300px;
    background: linear-gradient(160deg, var(--card-black) 0%, var(--card-black-deep) 100%);
    overflow: hidden;
  }
  .card--front { left: 40px; top: 250px; }
  .card--back { left: 620px; top: 250px; }

  .brand {
    position: absolute;
    display: flex;
    align-items: center;
    gap: 10px;
    color: var(--gold);
    font-weight: 700;
  }
  .brand__dot {
    width: 12px; height: 12px;
    border-radius: 50%;
    background: var(--gold);
  }
  .brand__name { letter-spacing: 1px; line-height: 1; }
  .brand__sub { display: block; font-size: 0.5em; letter-spacing: 0.5px; margin-top: 4px; text-align: right; }

  .card--front .brand { left: 70px; top: 62px; font-size: 34px; }
  .card--back .brand { left: 50%; top: 50%; transform: translate(-50%, -50%); font-size: 44px; }

  .slogan {
    position: absolute;
    left: 60px;
    top: 152px;
    width: 220px;
    text-align: right;
    color: var(--gold);
    font-weight: 700;
    font-size: 19px;
    line-height: 1.3;
  }

  .divider {
    position: absolute;
    left: 296px;
    top: 150px;
    width: 1px;
    height: 70px;
    background: var(--gold-dark);
  }

  .contacts {
    position: absolute;
    left: 312px;
    top: 150px;
    list-style: none;
    color: var(--gold);
    font-size: 14px;
  }
  .contacts li { display: flex; align-items: center; gap: 8px; height: 23px; }
  .contacts svg { width: 13px; height: 13px; flex: none; }

  .address-band {
    position: absolute;
    left: 0; right: 0;
    top: 250px;
    height: 24px;
    background: linear-gradient(90deg, var(--gold-dark) 0%, var(--gold) 35%, var(--gold-light) 70%, var(--gold) 100%);
    color: var(--band-text);
    font-size: 14px;
    line-height: 24px;
    padding-left: 150px;
  }
</style>
</head>
<body>

  <section class="card card--front" aria-label="Card front">
    <div class="brand">
      <span class="brand__dot"></span>
      <span class="brand__name">VELVADROME<span class="brand__sub">studio</span></span>
    </div>

    <p class="slogan">Your path to success<br>starts here</p>

    <span class="divider"></span>

    <ul class="contacts">
      <li>
        <svg viewBox="0 0 16 16" aria-hidden="true"><path fill="currentColor" d="M3.6 1.5l2.2 2.6-1.3 1.6c.9 2 2.4 3.5 4.3 4.3l1.6-1.3 2.6 2.2-1.4 2.3C7 13 3 9 1.8 3z"/></svg>
        0741263519
      </li>
      <li>
        <svg viewBox="0 0 16 16" aria-hidden="true"><rect x="1" y="3" width="14" height="10" fill="currentColor"/><path d="M1 3l7 6 7-6" fill="none" stroke="#1c1c1c" stroke-width="1.3"/></svg>
        infovelvadrome.ro
      </li>
      <li>
        <svg viewBox="0 0 16 16" aria-hidden="true"><circle cx="8" cy="8" r="6.5" fill="none" stroke="currentColor" stroke-width="1.5"/><path d="M1.5 8h13M8 1.5c-3 3.5-3 9.5 0 13M8 1.5c3 3.5 3 9.5 0 13" fill="none" stroke="currentColor" stroke-width="1.2"/></svg>
        www.velvadrome.ro
      </li>
    </ul>

    <div class="address-band">Your address, city, state, ZIP 0000</div>
  </section>

  <section class="card card--back" aria-label="Card back">
    <div class="brand">
      <span class="brand__dot"></span>
      <span class="brand__name">VELVADROME<span class="brand__sub">studio</span></span>
    </div>
  </section>

</body>
</html>
```